Harbinger Crude Advisors needs a logo design and business card layout.

HCA is a consulting firm in oil and gas, specializing in upstream engineering and field work. We provide engineering solutions for the complete wellbore cycle from casing design to flowback. This includes completion and production design. On-site job supervision and project engineering for conventional and unconventional reservoirs. Asset analysis by reviewing operational conditions of asset packages to determine value of potential acquisitions or divesture.

```html
<!DOCTYPE html>
<html lang="en">
<head>
<meta charset="utf-8">
<title>Harbinger Crude Advisors – Business Card</title>
<link rel="stylesheet" href="https://fonts.googleapis.com/css2?family=Bebas+Neue&family=PT+Sans:wght@400&family=PT+Sans+Narrow:wght@400&display=swap">
<style>
  :root {
    --backdrop: #999999;
    --card-light: #f1f1f1;
    --brand-blue: #1f78d6;
    --ink: #4a4a4a;
    --ink-soft: #5c5c5c;
    --rule: #cfcfcf;
    --white: #ffffff;
  }
  * { margin: 0; padding: 0; box-sizing: border-box; }
  html, body { width: 1200px; height: 900px; overflow: hidden; }
  body { background: var(--backdrop); position: relative; font-family: "PT Sans", Arial, sans-serif; }

  .card { position: absolute; width: 477px; height: 294px; }
  .card-front {
    left: 120px; top: 275px;
    background: var(--card-light);
    border-radius: 4px 50px 4px 50px;
  }
  .card-back {
    left: 607px; top: 273px;
    background: var(--brand-blue);
    border-radius: 50px 4px 50px 4px;
  }

  /* Front wordmark */
  .front-mark { position: absolute; right: 30px; top: 70px; display: flex; align-items: center; gap: 12px; color: var(--brand-blue); }
  .mark-square { width: 48px; height: 48px; background: var(--brand-blue); }
  .front-mark .mark-text { font-family: "Bebas Neue", Impact, sans-serif; line-height: 0.95; }
  .front-mark .mark-main { font-size: 44px; display: block; letter-spacing: 0.5px; }
  .front-mark .mark-sub { font-size: 21px; display: block; letter-spacing: 0.3px; }

  /* Person */
  .person { position: absolute; left: 30px; top: 160px; }
  .person-name { font-family: "PT Sans Narrow", "Arial Narrow", sans-serif; font-size: 20px; color: var(--ink-soft); text-transform: uppercase; line-height: 1; }
  .person-name .first { color: var(--brand-blue); }
  .person-role { font-size: 13px; color: var(--ink); margin-top: 1px; }
  .divider { position: absolute; left: 148px; top: 189px; width: 297px; height: 1px; background: var(--rule); }

  /* Address */
  .address { position: absolute; left: 31px; top: 235px; font-size: 13px; line-height: 17px; color: var(--ink); font-style: normal; }

  /* Contacts */
  .contacts { position: absolute; right: 26px; top: 200px; list-style: none; font-size: 13px; line-height: 17px; color: var(--ink); }
  .contacts li { display: flex; align-items: center; justify-content: flex-end; gap: 2px; }
  .contacts svg { width: 11px; height: 11px; fill: var(--brand-blue); flex: none; }

  /* Back wordmark */
  .back-mark { position: absolute; left: 0; right: 0; top: 66px; text-align: center; color: var(--white); }
  .back-mark .mark-square { width: 76px; height: 76px; background: var(--white); margin: 0 auto 18px; }
  .back-mark .mark-text { font-family: "Bebas Neue", Impact, sans-serif; line-height: 0.95; }
  .back-mark .mark-main { font-size: 50px; display: block; }
  .back-mark .mark-sub { font-size: 23px; display: block; }
</style>
</head>
<body>
  <section class="card card-front" aria-label="Business card front">
    <div class="front-mark">
      <span class="mark-square" aria-hidden="true"></span>
      <span class="mark-text">
        <span class="mark-main">Harbinger</span>
        <span class="mark-sub">Crude Advisors</span>
      </span>
    </div>

    <div class="person">
      <p class="person-name"><span class="first">Marcus</span> Ellery</p>
      <p class="person-role">Managing Director</p>
    </div>
    <span class="divider" aria-hidden="true"></span>

    <ul class="contacts">
      <li>044-555 010 220
        <svg viewBox="0 0 12 12" aria-hidden="true"><path d="M1 4c0-2 1.5-3 5-3s5 1 5 3v1H8.5V3.8c-1.6-.5-3.4-.5-5 0V5H1zM2.5 6h7l1 4.5H1.5z"/></svg>
      </li>
      <li>044-555 010 220
        <svg viewBox="0 0 12 12" aria-hidden="true"><path d="M3.5 0h5a1 1 0 0 1 1 1v10a1 1 0 0 1-1 1h-5a1 1 0 0 1-1-1V1a1 1 0 0 1 1-1zm.5 1.5v7.5h4V1.5zM6 9.8a.7.7 0 1 0 0 1.4.7.7 0 0 0 0-1.4z"/></svg>
      </li>
      <li>info@harbingercrude.com
        <svg viewBox="0 0 12 12" aria-hidden="true"><path d="M0 2h12v8H0zm1 1v.4l5 3.3 5-3.3V3zm0 1.6V9h10V4.6L6 8z"/></svg>
      </li>
      <li>www.harbingercrude.com
        <svg viewBox="0 0 12 12" aria-hidden="true"><circle cx="6" cy="6" r="6"/><path d="M3 3.5c1 .3 1.5 1 1.2 2-.3.8.5 1.3 1 1.8.3.5 0 1.5-.4 2.2M8 2c-.5 1 0 1.6.8 1.8.7.2 1 .8 1.5 1.5" stroke="#fff" stroke-width=".9" fill="none"/></svg>
      </li>
    </ul>

    <address class="address">4810 Derrick Lane, Suite 12<br>Midland, TX 79701</address>
  </section>

  <section class="card card-back" aria-label="Business card back">
    <div class="back-mark">
      <span class="mark-square" aria-hidden="true"></span>
      <span class="mark-text">
        <span class="mark-main">Harbinger</span>
        <span class="mark-sub">Crude Advisors</span>
      </span>
    </div>
  </section>
</body>
</html>
```